New Business Card Needed

I need a new business card for Meridale Kitchen & Bath.
Logo is attached as well a my photo. Note: Make the logo Navy Blue.
Here is the text:
Gregory Tenwick
GC/Owner
Charlotte NC
704-555-0139
gregory@meridaleHVX.com
www.meridaleHVX.com
Tag line on card: BEAUTY | FUNCTION | ON TIME | ON BUDGET
Trim size: 2.56" X 2.56"
This is where we aim to cut the cards.
Safe area: 2.4" X 2.4"
Make sure any important aspects of your design such as text and logos are inside of the safe area, otherwise they may be cut off.
Bleed area: 2.71 X 2.71
Make sure that your background extends to fill the bleed to avoid your Business Cards having white edges when trimmed.
On the back side. Use photo of kitchen attached.

```html
<!DOCTYPE html>
<html lang="en">
<head>
<meta charset="utf-8">
<title>Meridale Kitchen &amp; Bath – Business Card</title>
<link rel="stylesheet" href="https://fonts.googleapis.com/css2?family=Poppins:wght@400;500;600;700&display=swap">
<style>
  :root {
    --navy: #0b0d8a;
    --white: #ffffff;
    --cyan: #3cd2e6;
    --page: #eeeae4;
    --rule: rgba(255,255,255,0.45);
    --kitchen-light: #8583ad;
    --kitchen-mid: #5f5d8b;
    --kitchen-dark: #3b3a5e;
  }
  * { box-sizing: border-box; margin: 0; padding: 0; }
  html, body { width: 1200px; height: 1200px; overflow: hidden; }
  body {
    background: var(--page);
    font-family: "Poppins", sans-serif;
    position: relative;
  }
  .card {
    position: absolute;
    top: 330px;
    width: 540px;
    height: 540px;
    overflow: hidden;
  }
  .card-front { left: 40px; background: var(--navy); color: var(--white); }
  .card-back { left: 620px; }

  /* front */
  .portrait {
    position: absolute; left: 32px; top: 56px; width: 182px; height: 176px;
    background: linear-gradient(160deg, #6d6d6d, #3a3a3a);
  }
  .identity { position: absolute; left: 244px; top: 46px; width: 266px; }
  .identity-name { font-size: 25px; font-weight: 600; line-height: 1.3; }
  .identity-title { font-size: 20px; font-weight: 400; margin-top: 4px; }
  .identity-rule { height: 1px; background: var(--rule); margin: 22px 0 20px; }
  .contact-line { display: flex; align-items: center; gap: 14px; font-size: 19px; margin-bottom: 10px; }
  .contact-line svg { width: 14px; height: 14px; flex: none; fill: var(--cyan); }

  .brand-band {
    position: absolute; left: 22px; right: 0; top: 254px; height: 172px;
    background: var(--white); color: var(--navy);
    display: flex; align-items: center;
  }
  .tagline {
    width: 200px; text-align: right; font-size: 22px; font-weight: 400;
    line-height: 1.45; letter-spacing: 0.5px;
  }
  .wordmark { display: flex; align-items: center; gap: 14px; margin-left: 26px; }
  .wordmark-square { width: 22px; height: 22px; background: var(--navy); flex: none; }
  .wordmark-name { font-size: 26px; font-weight: 500; line-height: 1.15; letter-spacing: 0.5px; }

  .footer-links {
    position: absolute; left: 34px; right: 20px; bottom: 48px;
    display: flex; gap: 26px; font-size: 15px;
  }
  .footer-links span { display: flex; align-items: center; gap: 8px; }
  .footer-links svg { width: 11px; height: 11px; fill: var(--cyan); flex: none; }

  /* back */
  .kitchen-photo {
    position: absolute; inset: 0;
    background: linear-gradient(180deg, var(--kitchen-light) 0%, var(--kitchen-mid) 55%, var(--kitchen-dark) 100%);
  }
  .back-wordmark {
    position: absolute; left: 0; right: 0; top: 215px;
    display: flex; justify-content: center; align-items: center; gap: 14px;
    color: var(--white);
  }
  .back-wordmark .wordmark-square { background: var(--white); }
  .back-wordmark .wordmark-name { font-size: 32px; }
  .back-url {
    position: absolute; left: 0; right: 0; bottom: 62px; text-align: center;
    color: var(--white); font-size: 17px; letter-spacing: 1px;
  }
</style>
</head>
<body>

<section class="card card-front">
  <div class="portrait" role="img" aria-label="Portrait photo of Gregory Tenwick"></div>

  <div class="identity">
    <p class="identity-name">Gregory Tenwick</p>
    <p class="identity-title">GC/Owner</p>
    <div class="identity-rule"></div>
    <p class="contact-line">
      <svg viewBox="0 0 24 24"><path d="M12 2a7 7 0 0 0-7 7c0 5 7 13 7 13s7-8 7-13a7 7 0 0 0-7-7zm0 9.5A2.5 2.5 0 1 1 12 6.5a2.5 2.5 0 0 1 0 5z"/></svg>
      Charlotte, NC
    </p>
    <p class="contact-line">
      <svg viewBox="0 0 24 24"><path d="M6.6 10.8a15 15 0 0 0 6.6 6.6l2.2-2.2a1 1 0 0 1 1-.25 11.4 11.4 0 0 0 3.6.6 1 1 0 0 1 1 1V20a1 1 0 0 1-1 1A17 17 0 0 1 3 4a1 1 0 0 1 1-1h3.5a1 1 0 0 1 1 1c0 1.25.2 2.45.6 3.6a1 1 0 0 1-.25 1z"/></svg>
      704-555-0139
    </p>
  </div>

  <div class="brand-band">
    <p class="tagline">BEAUTY<br>FUNCTION<br>ON TIME<br>ON BUDGET</p>
    <div class="wordmark">
      <span class="wordmark-square"></span>
      <p class="wordmark-name">Meridale<br>Kitchen &amp; Bath</p>
    </div>
  </div>

  <div class="footer-links">
    <span>
      <svg viewBox="0 0 24 24"><path d="M2 5h20v14H2zm2 2v.5l8 5 8-5V7z"/></svg>
      gregory@meridaleHVX.com
    </span>
    <span>
      <svg viewBox="0 0 24 24"><circle cx="12" cy="12" r="10"/></svg>
      www.meridaleHVX.com
    </span>
  </div>
</section>

<section class="card card-back">
  <div class="kitchen-photo" role="img" aria-label="Photo of a white kitchen with cabinets, open shelves and an oven"></div>
  <div class="back-wordmark">
    <span class="wordmark-square"></span>
    <p class="wordmark-name">Meridale Kitchen &amp; Bath</p>
  </div>
  <p class="back-url">www.meridaleHVX.com</p>
</section>

</body>
</html>
```